Website for a web design agency

We are a website and marketing agency. We do website design, development, and well as Brindle and Quorvia advertising and analytics. We ourselves need a new website for our own brand. We are working on some designs in-house with our own designers, but we also wanted to see what outside designers would come up with.
We are starting off with the homepage, and here is the breakdown of the sections:
https://files.brindlework.example/sheet/d/7kqTr2VnPLwXeHsaMcY4oBfJzuGNtKdWiEh3Rx9pLmQb/view?mode=share
This doc also has many links to sites we have done, which you can take screenshots of for the portfolio section.
In terms of the "look" I am going for, I want to look high-end and very beautiful designs. I found this website that I like a lot that you can use some of the elements of, just as a starting point:
http://velmarkstudio.example/layouts/pixelbarn/html/ostrevo/index.html and here is another design option they have http://velmarkstudio.example/layouts/pixelbarn/html/ostrevo/index-4.html
I'm also uploading my logo. The logo matches the gold and black look from these websites, but I would be open to switching to another color scheme if needed.
This is the link to my very old website, which you can use for some of the dummy text, and a pic of myself. I will be taking more pics of myself:
https://theplumtreeandwillowgroup.example/
We need a homepage and a portfolio page right now, but if you are the winner, we will be hiring you to make additional pages.
Updates
More designs continue to come in even today, and I want to make sure no other designers are still submitting designs.
Target Market(s)
medium and large businesses owners, and non-profits
Number of Pages Required
1 page

```html
<!DOCTYPE html>
<html lang="en">
<head>
<meta charset="utf-8">
<title>Calvero Strategies — We Build Value</title>
<link href="https://fonts.googleapis.com/css2?family=Montserrat:wght@400;500;600;700;800&family=Open+Sans:ital,wght@0,400;0,600;1,400&display=swap" rel="stylesheet">
<style>
:root{
  --gold:#f8b31c;
  --ink:#1e1e1e;
  --dark:#232323;
  --darker:#1a1a1a;
  --grey:#8a8a8a;
  --line:#e4e4e4;
  --white:#ffffff;
}
*{margin:0;padding:0;box-sizing:border-box}
html,body{width:1200px;height:4295px;overflow:hidden}
body{position:relative;background:var(--white);font-family:"Open Sans",sans-serif;color:var(--ink)}
.abs{position:absolute}
.head-font{font-family:"Montserrat",sans-serif}

/* header */
.site-header{position:absolute;left:0;top:0;width:1200px;height:77px;background:rgba(30,30,30,.82);z-index:5}
.brand{position:absolute;left:130px;top:12px;font-family:"Montserrat",sans-serif;font-weight:600;color:var(--gold);line-height:1}
.brand .name{font-size:30px;letter-spacing:4px;display:block}
.brand .sub{font-size:14px;letter-spacing:7px;display:block;margin-top:4px}
.main-nav a{position:absolute;top:29px;font-family:"Montserrat",sans-serif;font-size:12px;font-weight:500;color:#e8e8e8;text-decoration:none;letter-spacing:.5px}
.main-nav a.active{color:var(--gold)}
.nav-underline{position:absolute;left:382px;top:74px;width:74px;height:3px;background:var(--gold)}

/* hero */
.hero{position:absolute;left:0;top:0;width:1200px;height:700px;background:radial-gradient(ellipse at 50% 40%,#6d6d6d 0%,#4a4a4a 45%,#2c2c2c 100%)}
.hero-title{position:absolute;left:0;width:1200px;text-align:center;color:#fff;font-family:"Montserrat",sans-serif}
.hero-title.big{top:258px;font-size:60px;font-weight:700;letter-spacing:3px}
.hero-title.small{font-size:23px;font-weight:700;letter-spacing:1.5px}
.btn-gold{position:absolute;background:var(--gold);color:#fff;font-family:"Montserrat",sans-serif;font-weight:700;text-align:center}
.hero-cta{left:498px;top:398px;width:207px;height:44px;border-radius:22px;line-height:44px;font-size:12px;letter-spacing:1px}
.call-tab{position:absolute;left:1153px;top:197px;width:47px;height:250px;background:#1b1b1b}
.call-tab span{position:absolute;left:50%;top:50%;transform:translate(-50%,-50%) rotate(-90deg);white-space:nowrap;font-family:"Montserrat",sans-serif;font-size:16px;font-weight:600;color:#fff}
.call-tab span b{color:var(--gold);font-weight:500}

/* section headings */
.sec-head{position:absolute;left:0;width:1200px;text-align:center;font-family:"Montserrat",sans-serif}
.sec-num{font-size:12px;color:#555}
.sec-kicker{font-size:14px;letter-spacing:3px;color:#444}
.sec-title{font-size:32px;font-weight:700;letter-spacing:2px;color:var(--ink)}
.sec-rule{position:absolute;height:3px;width:57px;background:var(--gold)}
.dark-text .sec-num,.dark-text .sec-kicker{color:#ddd}
.dark-text .sec-title{color:#fff}

/* services */
.services-grid{position:absolute;left:147px;top:915px;width:925px;height:465px;border:1px solid var(--line)}
.cell{position:absolute;width:308px;height:232px}
.cell .num{position:absolute;font-family:"Montserrat",sans-serif;font-size:72px;font-weight:800;color:#ececec;line-height:1}
.cell h3{position:absolute;font-family:"Montserrat",sans-serif;font-size:17px;font-weight:700;color:var(--ink)}
.cell p{position:absolute;font-size:12px;line-height:17px;color:var(--grey);width:195px}
.cell svg{position:absolute}
.cell.featured{background:var(--gold);border-radius:22px;box-shadow:0 10px 25px rgba(0,0,0,.12)}
.cell.featured .num{color:rgba(255,255,255,.45)}
.cell.featured h3,.cell.featured p{color:#fff}

/* portfolio */
.portfolio{position:absolute;left:0;top:1478px;width:1200px;height:635px;background:var(--dark)}
.portfolio .label{position:absolute;left:138px;font-family:"Montserrat",sans-serif;color:#fff}
.project-title{font-size:22px;font-weight:700;letter-spacing:1px}
.project-tag{font-size:11px;letter-spacing:.5px}
.project-copy{font-family:"Open Sans",sans-serif;font-size:12px;line-height:23px;width:330px;color:#e0e0e0}
.view-btn{left:135px;top:1878px;width:167px;height:42px;line-height:42px;font-size:12px;letter-spacing:1px;box-shadow:4px 4px 0 -1px var(--dark),5px 5px 0 0 #fff}

/* testimonials */
.quote-card{position:absolute;left:558px;top:2358px;width:487px;height:258px;background:#fff;box-shadow:0 4px 20px rgba(0,0,0,.12)}
.quote-card p{position:absolute;left:80px;top:42px;width:355px;font-style:italic;font-size:13px;line-height:23px;color:#333}
.quote-mark{position:absolute;font-family:"Montserrat",sans-serif;font-size:64px;font-weight:800;color:#d6d6d6;line-height:1}

/* team */
.team{position:absolute;left:0;top:2773px;width:1200px;height:582px;background:var(--dark)}
.member{position:absolute;top:2955px;width:213px;height:250px;border:1px solid #4a4a4a;background:#262626}
.member .photo{position:absolute;left:10px;top:8px;width:193px;height:188px}
.member .who{position:absolute;left:16px;top:208px;color:#fff;font-family:"Montserrat",sans-serif}
.member .who b{display:block;font-size:15px;font-weight:600}
.member .who span{font-family:"Open Sans",sans-serif;font-size:11px;color:#ccc}
.member .links{position:absolute;right:14px;top:220px;display:flex;gap:10px}
.member .links i{display:block;width:9px;height:9px;border-radius:50%;background:#fff}
.member .links i:first-child{background:var(--gold)}

/* contact */
.contact{position:absolute;left:0;top:3355px;width:618px;height:538px;background:var(--gold)}
.contact-photo{position:absolute;left:618px;top:3355px;width:582px;height:538px;background:linear-gradient(135deg,#c9b9a5 0%,#8d7462 40%,#e4ddd4 75%,#a6a29c 100%)}
.contact-head{position:absolute;left:133px;font-family:"Montserrat",sans-serif;color:#fff}
.field{position:absolute;background:#fff;border:1px solid #e8a710;font-size:11px;color:#777;padding:15px 16px}
.send-btn{position:absolute;left:133px;top:3752px;width:152px;height:38px;background:var(--ink);color:#fff;font-family:"Montserrat",sans-serif;font-size:11px;font-weight:700;text-align:center;line-height:38px;letter-spacing:.5px}

/* footer */
.site-footer{position:absolute;left:0;top:3893px;width:1200px;height:347px;background:var(--dark);color:#fff}
.footer-bar{position:absolute;left:0;top:4240px;width:1200px;height:55px;background:#1a1a1a;text-align:center;line-height:55px;font-size:11px;color:#bbb}
.foot-h{position:absolute;top:80px;font-family:"Montserrat",sans-serif;font-size:12px;font-weight:700;letter-spacing:.5px}
.foot-small{position:absolute;font-size:10px;color:#ccc}
.foot-val{position:absolute;font-size:12px;color:#fff}
.foot-links{position:absolute;left:764px;top:112px;list-style:none;font-size:11px;line-height:26.5px;color:#ddd}
.touch{position:absolute;left:955px;font-size:10px;color:#ddd;letter-spacing:.5px;display:flex;align-items:center;gap:14px}
.touch i{display:block;width:14px;height:14px;border-radius:3px;background:var(--gold)}
.touch i.w{background:#fff}
</style>
</head>
<body>

<!-- HERO -->
<section class="hero" role="img" aria-label="Portrait of the agency founder, a bearded man in a white shirt against a grey wall"></section>
<svg class="abs" style="left:0;top:600px" width="1200" height="110" viewBox="0 0 1200 110" aria-hidden="true">
  <path d="M0 40 C200 90 380 30 600 55 C820 80 1000 20 1200 45 L1200 110 L0 110 Z" fill="rgba(255,255,255,.55)"/>
  <path d="M0 70 C220 110 420 55 620 75 C840 97 1010 55 1200 70 L1200 110 L0 110 Z" fill="#fff"/>
</svg>

<header class="site-header">
  <div class="brand"><span class="name">CALVERO</span><span class="sub">STRATEGIES</span></div>
  <nav class="main-nav">
    <a class="active" style="left:385px">ABOUT US</a>
    <a style="left:504px">SERVICES</a>
    <a style="left:619px">TEAM</a>
    <a style="left:706px">PORTFOLIO</a>
    <a style="left:834px">TESTIMONIALS</a>
    <a style="left:982px">CONTACT</a>
  </nav>
  <div class="nav-underline"></div>
</header>

<h1 class="hero-title big">WE BUILD VALUE</h1>
<p class="hero-title small" style="top:327px">ENTERPRISE LEVEL WEBSITE DEVELOPMENT</p>
<p class="hero-title small" style="top:355px">AND ONLINE MARKETING</p>
<div class="btn-gold hero-cta">SEE HOW WE DO IT</div>
<svg class="abs" style="left:569px;top:465px" width="66" height="66" viewBox="0 0 66 66" aria-label="Play video">
  <circle cx="33" cy="33" r="31" fill="none" stroke="#fff" stroke-width="2"/>
  <path d="M27 22 L44 33 L27 44 Z" fill="none" stroke="#fff" stroke-width="2" stroke-linejoin="round"/>
</svg>
<div class="call-tab"><span><b>CALL US</b> (+123) 4417 2096</span></div>

<!-- SERVICES -->
<div class="sec-head" style="top:777px"><div class="sec-num">01</div></div>
<div class="sec-head" style="top:795px"><div class="sec-kicker">OUR SERVICES</div></div>
<div class="sec-head" style="top:816px"><h2 class="sec-title">WHAT WE DO</h2></div>
<div class="sec-rule" style="left:575px;top:861px"></div>

<div class="services-grid">
  <svg class="abs" style="left:307px;top:0" width="1" height="465"><line x1="0.5" y1="0" x2="0.5" y2="465" stroke="#e4e4e4"/></svg>
  <svg class="abs" style="left:615px;top:0" width="1" height="465"><line x1="0.5" y1="0" x2="0.5" y2="465" stroke="#e4e4e4"/></svg>
  <svg class="abs" style="left:0;top:232px" width="925" height="1"><line x1="0" y1="0.5" x2="925" y2="0.5" stroke="#e4e4e4"/></svg>
</div>

<!-- row 1 -->
<div class="cell" style="left:147px;top:915px">
  <svg style="left:33px;top:40px" width="52" height="46" viewBox="0 0 52 46" fill="none" stroke="#333" stroke-width="2"><rect x="2" y="2" width="48" height="32" rx="2"/><rect x="8" y="8" width="36" height="20" stroke="#f8b31c"/><path d="M20 34 L18 42 M32 34 L34 42 M12 43 H40"/></svg>
  <div class="num" style="left:28px;top:120px">1</div>
  <h3 style="left:80px;top:130px">Websites</h3>
  <p style="left:80px;top:156px">Lorem Ipsum is simply dummy text of the printing typesettin</p>
</div>
<div class="cell featured" style="left:445px;top:910px;width:323px;height:250px">
  <svg style="left:48px;top:48px" width="46" height="42" viewBox="0 0 46 42" fill="none" stroke="#fff" stroke-width="2"><rect x="2" y="2" width="42" height="32"/><path d="M8 26 L18 16 L26 24 L32 18 L38 26"/><line x1="2" y1="9" x2="44" y2="9"/></svg>
  <div class="num" style="left:30px;top:128px">2</div>
  <h3 style="left:85px;top:135px">Landing pages</h3>
  <p style="left:85px;top:161px;width:215px">Lorem Ipsum is simply dummy text of the printing and typesettin</p>
  <svg style="left:268px;top:200px" width="32" height="32" viewBox="0 0 32 32"><circle cx="16" cy="16" r="15" fill="#fff"/><path d="M9 16 H23 M18 11 L23 16 L18 21" stroke="#333" stroke-width="2" fill="none"/></svg>
</div>
<div class="cell" style="left:763px;top:915px">
  <svg style="left:45px;top:40px" width="54" height="48" viewBox="0 0 54 48" fill="none" stroke="#333" stroke-width="2"><rect x="2" y="2" width="50" height="30" rx="2"/><path d="M8 20 C14 10 22 24 28 14 C34 8 40 18 46 12" stroke="#f8b31c"/><rect x="18" y="36" width="18" height="10"/></svg>
  <div class="num" style="left:30px;top:120px">3</div>
  <h3 style="left:87px;top:130px">Donation Pages</h3>
  <p style="left:87px;top:156px">Lorem Ipsum is simply dummy text of the printing typesettin</p>
</div>
<!-- row 2 -->
<div class="cell" style="left:147px;top:1148px">
  <svg style="left:35px;top:42px" width="56" height="52" viewBox="0 0 56 52" fill="none" stroke="#333" stroke-width="2"><rect x="2" y="8" width="38" height="28" rx="2"/><circle cx="46" cy="10" r="8"/><path d="M46 5 V15" /><path d="M20 30 L24 46 L28 40 L34 44" stroke="#f8b31c"/><circle cx="20" cy="30" r="6" stroke="#f8b31c"/></svg>
  <div class="num" style="left:25px;top:125px">4</div>
  <h3 style="left:82px;top:125px">PPC and Funnels</h3>
  <p style="left:82px;top:151px;width:215px">Lorem Ipsum is simply dummy text of the printing and typesettin</p>
</div>
<div class="cell" style="left:455px;top:1148px">
  <svg style="left:35px;top:42px" width="52" height="48" viewBox="0 0 52 48" fill="none" stroke="#333" stroke-width="2"><path d="M2 6 H22 L26 10 L30 6 H50 V40 H30 L26 44 L22 40 H2 Z"/><circle cx="26" cy="26" r="7" stroke="#f8b31c"/><path d="M24 23 L30 26 L24 29 Z" stroke="#f8b31c"/><path d="M8 14 H18 M34 14 H44"/></svg>
  <div class="num" style="left:17px;top:125px">5</div>
  <h3 style="left:78px;top:125px">Video marketing</h3>
  <p style="left:78px;top:151px;width:215px">Lorem Ipsum is simply dummy text of the printing and typesettin</p>
</div>
<div class="cell" style="left:763px;top:1148px">
  <svg style="left:30px;top:42px" width="52" height="50" viewBox="0 0 52 50" fill="none" stroke="#333" stroke-width="2"><rect x="2" y="2" width="48" height="32" rx="2"/><path d="M8 26 L18 16 L26 22 L40 8" stroke="#f8b31c"/><path d="M8 42 H44 M14 38 V46 M26 38 V46 M38 38 V46"/></svg>
  <div class="num" style="left:17px;top:128px">6</div>
  <h3 style="left:82px;top:125px;line-height:22px">Analytics and<br>optimization</h3>
  <p style="left:82px;top:173px;width:215px">Lorem Ipsum is simply dummy text of the printing and typesettin</p>
</div>

<!-- PORTFOLIO -->
<section class="portfolio dark-text"></section>
<svg class="abs" style="left:560px;top:1515px" width="480" height="535" viewBox="0 0 480 535" aria-hidden="true"><ellipse cx="240" cy="267" rx="240" ry="267" fill="#f8b31c"/></svg>
<div class="label sec-num head-font" style="top:1584px;font-size:12px">02</div>
<div class="label head-font" style="top:1603px;font-size:14px;letter-spacing:3px">PROJECTS</div>
<h2 class="label head-font" style="top:1620px;font-size:33px;font-weight:700;letter-spacing:2px">PORTFOLIO</h2>
<h3 class="label project-title" style="top:1710px">ORVANE PRODUCTION</h3>
<div class="label project-tag" style="top:1748px">BRINGING YOU THE ENTERTAINMENT YOU LOVE</div>
<p class="label project-copy" style="top:1777px">Lorem Ipsum is simply dummy text of the printing and typesetting industry. Lorem Ipsum has been the industry's standard dummy text ever</p>
<div class="btn-gold view-btn">VIEW SITE</div>

<!-- laptop -->
<div class="abs" style="left:586px;top:1604px;width:503px;height:345px;background:#2a2a2a;border-radius:10px 10px 0 0"></div>
<div class="abs" style="left:596px;top:1620px;width:482px;height:320px;background:#fff"></div>
<div class="abs" role="img" aria-label="Website screenshot: entertainment studio homepage with a hero banner and a row of film posters" style="left:596px;top:1630px;width:482px;height:148px;background:linear-gradient(120deg,#0e1a3a 0%,#1e3d7a 55%,#0b1530 100%)"></div>
<div class="abs head-font" style="left:596px;top:1670px;width:400px;text-align:center;color:#fff;font-size:24px;font-weight:500;letter-spacing:.5px"><b style="font-weight:700">ORVANE</b> PRODUCTIONS</div>
<div class="abs head-font" style="left:596px;top:1805px;width:460px;text-align:center;color:#3a57a8;font-size:11px;font-weight:600;letter-spacing:1px">OUR PRODUCTIONS</div>
<div class="abs" role="img" aria-label="Row of film poster thumbnails" style="left:620px;top:1842px;width:430px;height:80px;background:linear-gradient(90deg,#3a2a1e,#6a5a3a 25%,#b9b2a6 40%,#22426e 60%,#0d1b33 80%,#5a3a2a)"></div>
<div class="abs" style="left:560px;top:1940px;width:586px;height:12px;background:#555;border-radius:0 0 8px 8px"></div>
<!-- phone -->
<div class="abs" style="left:502px;top:1745px;width:118px;height:250px;background:#1b1b1b;border-radius:12px"></div>
<div class="abs" style="left:508px;top:1758px;width:106px;height:228px;background:#fff"></div>
<div class="abs head-font" style="left:508px;top:1768px;width:106px;text-align:center;font-size:8px;font-weight:700">ORVANE</div>
<div class="abs" role="img" aria-label="Mobile view of the studio homepage" style="left:508px;top:1800px;width:106px;height:140px;background:linear-gradient(160deg,#1e3d7a,#0d1b33)"></div>
<div class="abs head-font" style="left:508px;top:1962px;width:106px;text-align:center;font-size:7px;font-weight:700;letter-spacing:1px">KNOWN FOR</div>
<svg class="abs" style="left:790px;top:1993px" width="90" height="22" viewBox="0 0 90 22" aria-label="Previous and next project"><path d="M2 11 H32 M10 3 L2 11 L10 19" stroke="#fff" stroke-width="2" fill="none"/><path d="M56 11 H86 M78 3 L86 11 L78 19" stroke="#fff" stroke-width="2" fill="none"/></svg>

<!-- TESTIMONIALS -->
<div class="sec-head" style="left:-2px;top:2180px"><div class="sec-num">03</div></div>
<div class="sec-head" style="left:-2px;top:2200px"><div class="sec-kicker">TESTIMONIALS</div></div>
<div class="sec-head" style="left:-2px;top:2218px"><h2 class="sec-title">CASE STUDIES</h2></div>
<div class="sec-rule" style="left:571px;top:2263px"></div>

<svg class="abs" style="left:138px;top:2250px" width="220" height="240" aria-hidden="true"><path d="M218 2 H3 V237 H24" stroke="#f8b31c" stroke-width="5" fill="none"/></svg>
<div class="abs" role="img" aria-label="Black and white photo of a smiling client holding a tablet in an office" style="left:188px;top:2308px;width:405px;height:360px;background:linear-gradient(135deg,#cfcfcf 0%,#8c8c8c 45%,#e6e6e6 70%,#5a5a5a 100%)"></div>
<svg class="abs" style="left:812px;top:2500px" width="240" height="122" aria-hidden="true"><path d="M236 0 V118 H2" stroke="#f8b31c" stroke-width="5" fill="none"/></svg>
<div class="quote-card">
  <div class="quote-mark" style="left:28px;top:32px">“</div>
  <p>Lorem Ipsum is simply dummy text of the printing and typesetting industry. Lorem Ipsum has been the industry's standard dummy text ever since the 1500s, when an unknown printer took a galley of type and scrambled it to make a specimen</p>
  <div class="quote-mark" style="left:295px;top:132px;font-size:40px">”</div>
  <div class="abs head-font" style="left:82px;top:170px;font-size:16px;font-weight:700">Idris Monteau</div>
  <div class="abs" style="left:82px;top:196px;font-size:11px;color:#555">Website/company name</div>
  <div class="abs" style="left:245px;top:184px;font-size:20px;color:var(--gold);letter-spacing:1px">★★★★★</div>
</div>
<svg class="abs" style="left:93px;top:2468px" width="36" height="20" aria-label="Previous testimonial"><path d="M2 10 H34 M10 2 L2 10 L10 18" stroke="#999" stroke-width="2" fill="none"/></svg>
<svg class="abs" style="left:1070px;top:2467px" width="36" height="20" aria-label="Next testimonial"><path d="M2 10 H34 M26 2 L34 10 L26 18" stroke="#222" stroke-width="2" fill="none"/></svg>

<!-- TEAM -->
<section class="team"></section>
<div class="sec-head dark-text" style="left:-6px;top:2820px"><div class="sec-num">04</div></div>
<div class="sec-head dark-text" style="left:-6px;top:2842px"><div class="sec-kicker">MEET TEAM</div></div>
<div class="sec-head dark-text" style="left:-6px;top:2860px"><h2 class="sec-title" style="font-size:33px">OUR TEAM</h2></div>
<div class="sec-rule" style="left:568px;top:2904px"></div>

<div class="member" style="left:132px">
  <div class="photo" role="img" aria-label="Team member portrait, woman in a white shirt" style="background:linear-gradient(160deg,#e9e6e2,#a89888)"></div>
  <div class="who"><b>Jone Due</b><span>Designation Post</span></div>
  <div class="links"><i></i><i></i><i></i></div>
</div>
<div class="member" style="left:372px">
  <div class="photo" role="img" aria-label="Team member portrait, woman in a dark blazer" style="background:linear-gradient(160deg,#ececec,#3a3f4c)"></div>
  <div class="who"><b>Jone Due</b><span>Designation Post</span></div>
  <div class="links"><i></i><i></i><i></i></div>
</div>
<div class="member" style="left:613px">
  <div class="photo" role="img" aria-label="Team member portrait, man in a grey suit" style="background:linear-gradient(160deg,#f0f0f0,#8a8a8a)"></div>
  <div class="who"><b>Jone Due</b><span>Designation Post</span></div>
  <div class="links"><i></i><i></i><i></i></div>
</div>
<div class="member" style="left:850px">
  <div class="photo" role="img" aria-label="Team member portrait, man with glasses in a navy shirt" style="background:linear-gradient(160deg,#e4e4e4,#2c3a52)"></div>
  <div class="who"><b>Jone Due</b><span>Designation Post</span></div>
  <div class="links"><i></i><i></i><i></i></div>
</div>

<!-- CONTACT -->
<section class="contact"></section>
<div class="contact-photo" role="img" aria-label="Two colleagues working together at a laptop in a bright office"></div>
<div class="contact-head" style="top:3402px;font-size:12px">05</div>
<div class="contact-head" style="top:3422px;font-size:14px;letter-spacing:3px">CONTACT US</div>
<div class="contact-head" style="top:3443px;font-size:27px;font-weight:500;letter-spacing:1px">GET A FREE AUDIT</div>
<div class="contact-head" style="top:3477px;font-size:27px;font-weight:700;letter-spacing:1px">AND CONSULTATION</div>
<div class="abs" style="left:133px;top:3522px;width:58px;height:3px;background:#fff"></div>
<div class="field" style="left:130px;top:3548px;width:212px;height:42px">First Name</div>
<div class="field" style="left:351px;top:3548px;width:213px;height:42px">Last Name</div>
<div class="field" style="left:130px;top:3600px;width:212px;height:42px">Email address</div>
<div class="field" style="left:351px;top:3600px;width:213px;height:42px">Phone</div>
<div class="field" style="left:130px;top:3652px;width:437px;height:92px">Leave message</div>
<div class="send-btn">SEND MESSAGE</div>

<!-- FOOTER -->
<footer class="site-footer">
  <div class="brand" style="left:138px;top:92px"><span class="name" style="font-size:40px;letter-spacing:5px">CALVERO</span><span class="sub" style="font-size:17px;letter-spacing:9px;margin-top:6px">STRATEGIES</span></div>
  <p class="abs" style="left:138px;top:172px;width:220px;font-size:10px;line-height:15px;color:#ccc">Lorem Ipsum is simply dummy text of the printing and typesetting industry. Lorem Ipsum has been industry's standard</p>

  <h4 class="foot-h" style="left:473px">CONTACT US</h4>
  <svg class="abs" style="left:478px;top:127px" width="26" height="26" viewBox="0 0 24 24" fill="none" stroke="#f8b31c" stroke-width="1.6"><path d="M5 3 L9 3 L11 8 L8 10 C9.5 13 11 14.5 14 16 L16 13 L21 15 L21 19 C21 20 20 21 19 21 C10 21 3 14 3 5 C3 4 4 3 5 3 Z"/></svg>
  <div class="foot-small" style="left:528px;top:117px">Phone Number</div>
  <div class="foot-val" style="left:528px;top:133px">(+958) 4417 2096</div>
  <svg class="abs" style="left:478px;top:185px" width="28" height="22" viewBox="0 0 28 22" fill="none" stroke="#f8b31c" stroke-width="1.6"><rect x="1" y="1" width="26" height="20"/><path d="M1 2 L14 12 L27 2"/></svg>
  <div class="foot-small" style="left:528px;top:177px">Email address</div>
  <div class="foot-val" style="left:528px;top:193px">info@calvero.example</div>
  <svg class="abs" style="left:481px;top:238px" width="22" height="28" viewBox="0 0 22 28" fill="none" stroke="#f8b31c" stroke-width="1.6"><path d="M11 27 C5 19 2 14 2 10 A9 9 0 0 1 20 10 C20 14 17 19 11 27 Z"/><circle cx="11" cy="10" r="3.5"/></svg>
  <div class="foot-small" style="left:528px;top:237px">Office address</div>
  <div class="foot-val" style="left:528px;top:253px">22/B Harbor Lane, Fairview</div>

  <h4 class="foot-h" style="left:762px">NAVIGATION</h4>
  <ul class="foot-links">
    <li>Home</li><li>About Us</li><li>Services</li><li>Portfolio</li><li>Testimonials</li><li>Contact Us</li>
  </ul>

  <h4 class="foot-h" style="left:950px">GET IN TOUCH</h4>
  <div class="touch" style="top:119px"><i></i>QUORVIA</div>
  <div class="touch" style="top:155px"><i class="w"></i>CHIRPLINE</div>
  <div class="touch" style="top:191px"><i class="w"></i>LINKVALE</div>
</footer>
<div class="footer-bar">Copyright 2021 Calvero Strategies.example All Right Reserved</div>

</body>
</html>
```